KELP clinical trial results infographic

We need an infographic which presents the results from the KELP research trial. It should be colourful and engaging, in understandable language and showing the steps to get to the results. This is to showcase the results to patients/the public/clinicians, giving a brief summary of what the study proved. The final design should have the KELP logo at the top (please see the logo on the attached Word document)
I have attached the required logos which need to be used (KELP - within the Word doc, Brindlemoor Injury and Acute Care, University of Caddering, QRV - see also their design pack attached) as well as an example from another study, PLUMBEX4, as an example of what the layout could look like. Please DO NOT use the content from the PLUMBEX4 example though, please instead use the content from the attached document 'InfographicDesignInformation_KELP_ArtHatchery_02Dec2025'. Please also include information about the funding in a footer at the bottom of the infographic (as per the above document).
Look and feel
Each slider illustrates characteristics of the customer's brand and the style your logo design should communicate.

```html
<!DOCTYPE html>
<html lang="en">
<head>
<meta charset="utf-8">
<title>KELP Trial Results Infographic</title>
<link href="https://fonts.googleapis.com/css2?family=Montserrat:wght@300;400;700;800&family=Oswald:wght@500;600&family=Poppins:wght@400;500;600;700&display=swap" rel="stylesheet">
<style>
  :root{
    --navy:#1c3566;
    --navy-deep:#0f2a5c;
    --blue:#2477c2;
    --blue-mid:#2b6fb8;
    --panel:#c9e0f4;
    --orange:#eb6319;
    --orange-light:#f2801f;
    --orange-deep:#e24a17;
    --white:#ffffff;
    --ink:#1b1b1b;
  }
  *{box-sizing:border-box;margin:0;padding:0}
  html,body{width:844px;height:1200px;overflow:hidden;background:var(--white)}
  body{font-family:"Poppins",sans-serif;color:var(--ink);position:relative}
  .abs{position:absolute}
  .condensed{font-family:"Oswald",sans-serif;font-weight:600;text-transform:uppercase;color:var(--navy);letter-spacing:.2px}

  /* header */
  .brand{left:48px;top:16px}
  .brand-name{font-family:"Montserrat",sans-serif;font-weight:800;font-size:52px;line-height:1;color:var(--navy-deep);letter-spacing:-1px}
  .brand-sub{font-family:"Oswald",sans-serif;font-weight:600;font-size:10.5px;color:var(--navy-deep);margin-top:3px;letter-spacing:.1px}
  .hero-art{left:516px;top:0;width:274px;height:176px;border-radius:0 0 120px 140px;background:radial-gradient(circle at 62% 40%,#ffd23f 0,#f7a036 22%,#ef6b1f 40%,#f8c9a0 60%,#fbe4d2 100%)}

  /* panels */
  .panel{background:var(--panel)}
  .panel-main{left:23px;top:97px;width:551px;height:621px;border-radius:16px 16px 0 16px}
  .panel-side{left:560px;top:398px;width:260px;height:320px;border-radius:16px 16px 16px 0}
  .panel-join{left:560px;top:690px;width:20px;height:28px}

  .trial-tag{left:50px;top:124px;height:32px;padding:0 10px;background:var(--orange);color:var(--white);font-family:"Oswald",sans-serif;font-weight:500;font-size:17px;line-height:32px;border-radius:3px;white-space:nowrap}
  .headline{left:50px;top:164px;font-family:"Montserrat",sans-serif;color:var(--navy);font-size:34px;line-height:38px;white-space:nowrap}
  .headline b{font-weight:800}
  .headline span{font-weight:300}

  .methods{left:50px;top:300px;font-size:20px}

  .illus{border-radius:8px;border:1.5px solid var(--navy)}
  .illus-patient{left:50px;top:343px;width:100px;height:104px;background:linear-gradient(160deg,#fde3d3,#3d82c8 70%,#f1c42a)}
  .illus-doctor{left:284px;top:343px;width:104px;height:104px;background:linear-gradient(160deg,#ffffff,#cfe1f5 60%,#7aa7d8)}

  .pill-tag{height:18px;padding:0 7px;background:var(--blue-mid);color:var(--white);font-family:"Oswald",sans-serif;font-weight:500;font-size:10.5px;line-height:18px;border-radius:4px;white-space:nowrap}
  .stat-num{font-family:"Montserrat",sans-serif;font-weight:800;color:var(--navy);font-size:42px;line-height:1}
  .stat-label{font-family:"Poppins",sans-serif;color:var(--ink);font-size:12.5px;letter-spacing:1.6px}

  .groups-title{left:50px;top:470px;font-size:21.5px;white-space:nowrap}

  .pct{font-family:"Montserrat",sans-serif;font-weight:800;font-size:27px;line-height:1}
  .pct-delayed{left:60px;top:520px;color:var(--blue);display:flex;align-items:center;gap:5px}
  .pct-early{left:408px;top:520px;color:var(--orange);display:flex;align-items:center;gap:5px}
  .group-text{font-size:13px;line-height:16px;color:var(--ink)}
  .weeks{height:26px;padding:0 8px;color:var(--white);background:var(--blue-mid);font-family:"Montserrat",sans-serif;font-weight:800;font-size:16px;line-height:26px;letter-spacing:1px;border-radius:3px;white-space:nowrap}

  .donut{left:185px;top:506px}

  /* measured box */
  .measured{left:572px;top:419px;width:226px;height:282px;border:2px solid var(--navy);border-radius:12px}
  .measured-title{left:586px;top:430px;font-size:21px;white-space:nowrap}
  .measure-item{left:605px;display:flex;align-items:center;gap:10px;font-family:"Poppins",sans-serif;font-weight:600;font-size:13px;color:var(--navy)}
  .measure-icon{width:22px;height:22px;border-radius:50%;flex:none}
  .measured-at{left:667px;top:588px;font-size:12.5px;color:var(--ink)}
  .time-pill{left:667px;height:18px;padding:0 5px;background:var(--blue-mid);color:var(--white);font-family:"Poppins",sans-serif;font-weight:600;font-size:11.5px;line-height:18px;border-radius:3px;white-space:nowrap}
  .after{left:668px;top:670px;font-family:"Poppins",sans-serif;font-weight:700;font-size:12px;color:var(--ink)}

  /* background text */
  .bg-title{right:27px;top:163px;font-size:22px}
  .bg-text{right:27px;width:232px;text-align:right;font-size:11px;line-height:15px;color:var(--ink)}
  .bg-text.strong{font-weight:600}

  /* results */
  .results-banner{left:300px;top:718px;width:244px;height:44px;background:linear-gradient(90deg,var(--orange-light),var(--orange-deep));color:var(--white);font-family:"Montserrat",sans-serif;font-weight:800;font-size:27px;letter-spacing:4px;display:flex;align-items:center;justify-content:center;gap:10px;border-radius:0 0 6px 6px}
  .results-banner .star{color:#ffd23f;font-size:18px;letter-spacing:0}
  .result-card{top:782px;height:147px;border-radius:12px;overflow:hidden;padding:14px 14px}
  .card-safe{left:23px;width:256px;background:#244a86;color:var(--white)}
  .card-complications{left:300px;width:244px;background:var(--blue);color:var(--white)}
  .card-cost{left:566px;width:254px;background:var(--panel);color:var(--navy)}
  .card-title{position:relative;font-family:"Poppins",sans-serif;font-weight:600;font-size:16px;line-height:19px;z-index:1}
  .card-body{position:absolute;left:14px;bottom:12px;font-size:12.5px;line-height:15px;z-index:1}
  .card-cost .card-body{color:var(--ink)}
  .card-art{position:absolute;right:0;top:0;bottom:0}
  .card-safe .card-art{width:96px;background:linear-gradient(200deg,#f8b272,#e97a33 60%,#244a86 100%)}
  .card-complications .card-art{width:90px;background:linear-gradient(210deg,#f7c8a4,#f3dccb 60%,var(--blue) 100%)}
  .card-cost .card-art{width:80px;background:linear-gradient(190deg,#f4c23b,#f1a7a4 60%,var(--panel) 100%)}

  /* conclusion */
  .conclusion{left:23px;top:944px;width:797px;height:102px;border-radius:14px;background:linear-gradient(90deg,var(--orange-light),var(--orange-deep));color:var(--white);font-family:"Montserrat",sans-serif;font-size:19.5px;line-height:25px;text-align:center;display:flex;align-items:center;justify-content:center;letter-spacing:.6px}
  .conclusion span{font-weight:300}
  .conclusion b{font-weight:800}

  /* footer */
  .contact-box{left:25px;top:1068px;width:292px;height:38px;background:linear-gradient(90deg,#1f63ad,#0f4585);border-radius:3px;display:flex;align-items:center;gap:10px;padding:0 12px;color:var(--white);font-weight:600;font-size:15px}
  .contact-email{left:25px;top:1114px;font-size:21px;white-space:nowrap}
  .partner{font-family:"Poppins",sans-serif;color:#555;font-size:13px;display:flex;align-items:center;gap:6px;white-space:nowrap}
  .partner-mark{width:14px;height:14px;background:#c4203a;flex:none}
  .sponsor-title{left:356px;top:1068px;font-size:18px}
  .sponsor-block{left:363px;top:1092px;width:88px;height:86px;background:var(--navy-deep);color:var(--white);font-family:"Poppins",sans-serif;font-size:10px;line-height:12px;text-align:center;display:flex;align-items:flex-end;justify-content:center;padding:0 4px 12px}
  .fund-title{left:489px;top:1068px;font-size:18px}
  .fund-text{left:489px;font-size:10px;line-height:13px;font-weight:600;color:var(--ink);white-space:nowrap}
  .support-title{left:489px;top:1133px;font-size:18px}
  .qrv{left:680px;top:1147px;display:flex;align-items:center;gap:8px;font-family:"Poppins",sans-serif;font-weight:500;font-size:16px;line-height:17px;color:var(--navy-deep)}
  .qrv-mark{width:22px;height:22px;background:#f2c21b;flex:none}
</style>
</head>
<body>

  <!-- header -->
  <div class="abs brand">
    <div class="brand-name">KELP</div>
    <div class="brand-sub">WEIGHT-BEARING IN ANKLE FRACTURES</div>
  </div>
  <div class="abs hero-art" role="img" aria-label="Illustration of a foot and ankle skeleton with a glowing orange target over the ankle joint"></div>

  <!-- panels -->
  <div class="abs panel panel-main"></div>
  <div class="abs panel panel-side"></div>
  <div class="abs panel panel-join"></div>

  <div class="abs trial-tag">WEIGHT BEARING IN ANKLE FRACTURES (KELP TRIAL)</div>
  <h1 class="abs headline"><b>PATIENTS CAN START</b><br><b>WALKING</b> <span>EARLIER AFTER</span><br><span>ANKLE FRACTURE SURGERY</span></h1>

  <h2 class="abs condensed methods">Methods</h2>

  <div class="abs illus illus-patient" role="img" aria-label="Illustration of an adult patient"></div>
  <div class="abs pill-tag" style="left:166px;top:356px">(ADULTS AGED 18+)</div>
  <div class="abs stat-num" style="left:166px;top:382px">561</div>
  <div class="abs stat-label" style="left:168px;top:424px">PATIENTS</div>

  <div class="abs illus illus-doctor" role="img" aria-label="Illustration of a doctor beside a hospital building"></div>
  <div class="abs pill-tag" style="left:407px;top:356px">RANDOMIZED ACROSS</div>
  <div class="abs stat-num" style="left:407px;top:382px">23</div>
  <div class="abs stat-label" style="left:408px;top:424px;letter-spacing:.6px">HOSPITALS IN THE UK</div>

  <h2 class="abs condensed groups-title">Patients were randomly divided into two groups</h2>

  <!-- delayed group -->
  <div class="abs pct pct-delayed">
    <svg width="22" height="24" viewBox="0 0 22 24" aria-hidden="true"><rect x="8" y="0" width="6" height="3" rx="1" fill="var(--blue)"/><circle cx="11" cy="14" r="9" fill="none" stroke="var(--blue)" stroke-width="2.5"/><path d="M11 14V9" stroke="var(--blue)" stroke-width="2.2" stroke-linecap="round"/></svg>
    50%
  </div>
  <div class="abs group-text" style="left:60px;top:553px">Delayed<br>Weight-Bearing</div>
  <div class="abs group-text" style="left:60px;top:603px">Avoided<br>walking on the<br>operated leg for</div>
  <div class="abs weeks" style="left:58px;top:657px">6 WEEKS</div>

  <!-- early group -->
  <div class="abs pct pct-early">
    <svg width="22" height="24" viewBox="0 0 22 24" aria-hidden="true"><rect x="8" y="0" width="6" height="3" rx="1" fill="var(--orange)"/><circle cx="11" cy="14" r="9" fill="none" stroke="var(--orange)" stroke-width="2.5"/><path d="M11 14V9" stroke="var(--orange)" stroke-width="2.2" stroke-linecap="round"/></svg>
    50%
  </div>
  <div class="abs group-text" style="right:340px;top:553px;text-align:right">Early<br>Weight-Bearing</div>
  <div class="abs group-text" style="right:340px;top:606px;text-align:right">Started walking</div>
  <div class="abs weeks" style="left:402px;top:626px;background:var(--blue-mid)">2 WEEKS</div>
  <div class="abs group-text" style="right:340px;top:658px;text-align:right">after surgery, as<br>comfort allowed.</div>

  <!-- donut -->
  <svg class="abs donut" width="190" height="190" viewBox="0 0 190 190" aria-label="Pie chart: 50% delayed weight-bearing, 50% early weight-bearing">
    <defs>
      <linearGradient id="navyRing" x1="0" y1="0" x2="0" y2="1"><stop offset="0" stop-color="#1d3f7e"/><stop offset="1" stop-color="#2e7cc6"/></linearGradient>
      <linearGradient id="orangeRing" x1="0" y1="0" x2="0" y2="1"><stop offset="0" stop-color="#f07d1b"/><stop offset="1" stop-color="#e8501a"/></linearGradient>
    </defs>
    <circle cx="95" cy="95" r="92" fill="none" stroke="var(--navy)" stroke-width="0.8" stroke-dasharray="2 2"/>
    <circle cx="95" cy="95" r="66" fill="#d7e8f7"/>
    <path d="M93 173 A78 78 0 0 1 93 17" fill="none" stroke="url(#navyRing)" stroke-width="16"/>
    <path d="M97 17 A78 78 0 0 1 97 173" fill="none" stroke="url(#orangeRing)" stroke-width="16"/>
    <circle cx="95" cy="95" r="60" fill="#cfe3f6"/>
  </svg>
  <svg class="abs" width="844" height="30" style="left:0;top:524px" aria-hidden="true">
    <path d="M103 10H186L216 14" fill="none" stroke="var(--navy)" stroke-width="0.8"/><circle cx="189" cy="10" r="2" fill="var(--navy)"/><circle cx="217" cy="14" r="2" fill="var(--blue)"/>
    <path d="M409 10H372L345 14" fill="none" stroke="var(--navy)" stroke-width="0.8"/><circle cx="409" cy="10" r="2" fill="var(--orange)"/><circle cx="343" cy="14" r="2" fill="var(--orange)"/>
  </svg>
  <div class="abs" style="left:228px;top:548px;width:104px;height:104px;border-radius:50%;background:radial-gradient(circle,#f4f8fd 0,#d6e6f6 70%)" role="img" aria-label="X-ray style illustration of foot bones"></div>

  <!-- what was measured -->
  <div class="abs measured"></div>
  <h2 class="abs condensed measured-title">What was measured?</h2>
  <div class="abs measure-item" style="top:476px"><span class="measure-icon" style="background:linear-gradient(135deg,#f8c9a0,#e9eef6)" role="img" aria-label="Foot icon"></span>Ankle function</div>
  <div class="abs measure-item" style="top:513px">
    <svg class="measure-icon" viewBox="0 0 22 22" aria-hidden="true"><circle cx="11" cy="11" r="10" fill="#fff" stroke="var(--navy)" stroke-width="1.2"/><path d="M11 4L18 17H4Z" fill="#f8d12b" stroke="var(--navy)" stroke-width="1.2" stroke-linejoin="round"/><path d="M11 9v4" stroke="var(--navy)" stroke-width="1.5" stroke-linecap="round"/><circle cx="11" cy="15" r=".9" fill="var(--navy)"/></svg>
    Complications</div>
  <div class="abs measure-item" style="top:551px"><span class="measure-icon" style="background:linear-gradient(135deg,#e2e8f0,#ffffff)" role="img" aria-label="Icon of a content person"></span>Quality of life</div>
  <svg class="abs" width="56" height="98" viewBox="0 0 56 98" style="left:598px;top:587px" aria-label="Hourglass icon">
    <path d="M5 3H51C51 30 31 40 31 49C31 58 51 68 51 95H5C5 68 25 58 25 49C25 40 5 30 5 3Z" fill="#fff" stroke="var(--ink)" stroke-width="2.5" stroke-linejoin="round"/>
    <path d="M13 17H43C40 32 30 38 28 46C26 38 16 32 13 17Z" fill="var(--orange)"/>
    <path d="M28 72C33 80 40 86 44 91H12C16 86 23 80 28 72Z" fill="var(--blue)"/>
  </svg>
  <div class="abs measured-at">Measured at:</div>
  <div class="abs time-pill" style="top:607px">6 Weeks</div>
  <div class="abs time-pill" style="top:628px">4 Months</div>
  <div class="abs time-pill" style="top:649px">12 Months</div>
  <div class="abs after">AFTER SURGERY</div>

  <!-- background -->
  <h2 class="abs condensed bg-title">Background</h2>
  <p class="abs bg-text" style="top:201px">Ankle fractures are very common and often need an operation. After surgery, patients are usually told not to walk for six weeks.</p>
  <p class="abs bg-text" style="top:270px">But another option is to start walking two weeks after surgery, putting as much weight through the leg as feels comfortable.</p>
  <p class="abs bg-text strong" style="top:338px">The KELP study looked at which approach helps people recover safely and effectively.</p>

  <!-- results -->
  <div class="abs results-banner"><span class="star">&#9733;</span>RESULTS<span class="star">&#9733;</span></div>

  <div class="abs result-card card-safe">
    <div class="card-art" role="img" aria-label="Illustration of a foot with a dumbbell and a clinician with a magnifying glass"></div>
    <div class="card-title">Safe,<br>without waiting<br>6 weeks</div>
    <p class="card-body">Similar ankle<br>function with<br>early walking</p>
  </div>
  <div class="abs result-card card-complications">
    <div class="card-art" role="img" aria-label="Illustration of a bandaged ankle"></div>
    <div class="card-title">No<br>added<br>complications</div>
    <p class="card-body">Both groups<br>had similar<br>complication rates</p>
  </div>
  <div class="abs result-card card-cost">
    <div class="card-art" role="img" aria-label="Illustration of a hand dropping coins into a piggy bank"></div>
    <div class="card-title">Likely<br>to be<br>cost-effective</div>
    <p class="card-body">Costs were similar,<br>slightly lower with<br>early walking</p>
  </div>

  <div class="abs conclusion">
    <p><span>STARTING TO WALK EARLIER</span> <b>AFTER ANKLE SURGERY IS SAFE<br>FOR MOST PATIENTS</b> <span>AND LEADS TO</span> <b>SIMILAR RECOVERY<br>AS WAITING SIX WEEKS.</b></p>
  </div>

  <!-- footer -->
  <div class="abs contact-box">
    <svg width="26" height="18" viewBox="0 0 26 18" aria-hidden="true"><rect x="1" y="1" width="24" height="16" fill="#fff" stroke="#c9ced8"/><path d="M1 1L13 10L25 1" fill="none" stroke="#9aa3b3"/></svg>
    For more info write us at:
  </div>
  <div class="abs condensed contact-email">qrvhealth@caddering.ac.uk</div>
  <div class="abs partner" style="left:30px;top:1156px"><span class="partner-mark"></span>BRINDLEMOOR INJURY &amp; ACUTE CARE</div>

  <h3 class="abs condensed sponsor-title">Sponsored by</h3>
  <div class="abs sponsor-block">University of Caddering</div>

  <h3 class="abs condensed fund-title">Funded by</h3>
  <p class="abs fund-text" style="top:1093px">National Institute for Care Research (NICR),<br>Community Health Outcomes programme (CHO-RG-0000-10001)</p>
  <h3 class="abs condensed support-title">Supported by the</h3>
  <p class="abs fund-text" style="top:1157px">NICR Caddering Biomedical<br>Research Centre</p>
  <div class="abs qrv"><span class="qrv-mark"></span>QRV<br>Health</div>

</body>
</html>
```